Design Business Card CORAL TIDE MOWING

We have attached a copy of our Logo, we like a business card designed with logo and mobile phone number on one side that stands out maybe gloss and on the other side it can have the services we do small picture of our logo name number, I have attached an idea to this that I have seen online, this is a business owned by a woman so we like pinks black and navy
Our logo is attached in pdf
Target Market(s)
Home owners that need lawns mowed
Industry/Entity Type
Lawns and gardens
Contact Information for Business Card
Logo business Owner name Dorinda Pask mobile number 0417296054
Font styles to use
Look and feel
Each slider illustrates characteristics of the customer's brand and the style your logo design should communicate.

```html
<!DOCTYPE html>
<html lang="en">
<head>
<meta charset="utf-8">
<title>Coral Tide Mowing – Business Card</title>
<link rel="stylesheet" href="https://fonts.googleapis.com/css2?family=Open+Sans:wght@400;600;700;800&display=swap">
<style>
  :root {
    --stage: #232323;
    --card: #1f1e22;
    --card-band: #19181c;
    --card-band-deep: #141316;
    --pink: #e6168a;
    --green: #3cb84a;
    --white: #f4f4f6;
  }
  * { box-sizing: border-box; margin: 0; padding: 0; }
  html, body { width: 1200px; height: 780px; overflow: hidden; }
  body {
    background: var(--stage);
    font-family: "Open Sans", Arial, sans-serif;
    color: var(--white);
    position: relative;
  }
  .card {
    position: absolute;
    top: 70px;
    width: 366px;
    height: 640px;
    border-radius: 22px;
    background: var(--card);
    box-shadow: 0 14px 30px rgba(0,0,0,.55);
    overflow: hidden;
  }
  .card--front { left: 190px; }
  .card--back { left: 644px; }

  /* Brand lockup */
  .brand {
    position: absolute;
    left: 0; right: 0;
    display: flex;
    flex-direction: column;
    align-items: center;
    text-align: center;
  }
  .brand__dot {
    border-radius: 50%;
    background: var(--pink);
  }
  .brand__name {
    color: var(--pink);
    font-weight: 800;
    text-transform: uppercase;
    line-height: 1.05;
  }
  .card--front .brand { top: 210px; }
  .card--front .brand__dot { width: 110px; height: 110px; margin-bottom: 22px; }
  .card--front .brand__name { font-size: 34px; letter-spacing: 1px; }

  .card--back .brand { top: 48px; }
  .card--back .brand__dot { width: 54px; height: 54px; margin-bottom: 12px; }
  .card--back .brand__name { font-size: 20px; letter-spacing: .5px; }

  /* Contact block */
  .contact {
    position: absolute;
    top: 240px;
    left: 0; right: 0;
    text-align: center;
    z-index: 2;
  }
  .contact__name { font-size: 31px; font-weight: 700; line-height: 1.1; }
  .contact__first { color: var(--pink); }
  .contact__last { color: var(--green); }
  .contact__role { font-size: 14px; font-weight: 600; margin-top: 2px; }
  .contact__icons {
    display: flex;
    justify-content: center;
    gap: 8px;
    margin: 12px 0 10px;
  }
  .contact__icons svg { width: 24px; height: 24px; }
  .contact__line { font-size: 14.5px; line-height: 1.45; letter-spacing: .3px; }

  .card__bands {
    position: absolute;
    left: 0; bottom: 0;
    width: 366px; height: 300px;
  }

  .services {
    position: absolute;
    left: 24px; right: 24px;
    bottom: 58px;
    text-align: center;
    z-index: 2;
  }
  .services__title {
    color: var(--pink);
    font-size: 20px;
    font-weight: 700;
    letter-spacing: .5px;
    margin-bottom: 6px;
  }
  .services__list {
    list-style: none;
    display: flex;
    flex-wrap: wrap;
    justify-content: center;
    gap: 2px 12px;
    font-size: 13.5px;
  }
  .services__list li::before {
    content: "";
    display: inline-block;
    width: 7px; height: 7px;
    border-radius: 50%;
    background: var(--pink);
    margin-right: 5px;
    vertical-align: middle;
  }
</style>
</head>
<body>

<section class="card card--front" aria-label="Card front">
  <div class="brand">
    <span class="brand__dot"></span>
    <p class="brand__name">Coral Tide<br>Mowing</p>
  </div>
</section>

<section class="card card--back" aria-label="Card back">
  <div class="brand">
    <span class="brand__dot"></span>
    <p class="brand__name">Coral Tide Mowing</p>
  </div>

  <svg class="card__bands" viewBox="0 0 366 300" aria-hidden="true">
    <path d="M0 40 Q120 150 366 20 L366 300 L0 300 Z" fill="var(--card-band)"/>
    <path d="M0 110 Q170 170 366 90 L366 300 L0 300 Z" fill="var(--card-band-deep)"/>
  </svg>

  <div class="contact">
    <p class="contact__name"><span class="contact__first">Dorinda</span> <span class="contact__last">Pask</span></p>
    <p class="contact__role">Owner</p>
    <div class="contact__icons">
      <svg viewBox="0 0 24 24" aria-label="Phone"><circle cx="12" cy="12" r="12" fill="var(--pink)"/><path d="M8.5 6.5l2 2.2-1.2 1.4c.8 1.7 2 2.9 3.6 3.7l1.4-1.2 2.2 2-1.2 1.8c-4.4-.6-7.7-3.9-8.3-8.3z" fill="#fff"/></svg>
      <svg viewBox="0 0 24 24" aria-label="Email"><circle cx="12" cy="12" r="12" fill="var(--pink)"/><rect x="6" y="8" width="12" height="8.5" rx="1" fill="#fff"/><path d="M6.5 8.5l5.5 4.2 5.5-4.2" stroke="var(--pink)" stroke-width="1.3" fill="none"/></svg>
      <svg viewBox="0 0 24 24" aria-label="Website"><circle cx="12" cy="12" r="12" fill="var(--pink)"/><circle cx="12" cy="12" r="6" fill="none" stroke="#fff" stroke-width="1.4"/><path d="M6 12h12M12 6c-2.4 3.3-2.4 8.7 0 12M12 6c2.4 3.3 2.4 8.7 0 12" stroke="#fff" stroke-width="1.2" fill="none"/></svg>
    </div>
    <p class="contact__line">041 729 6054</p>
    <p class="contact__line">info@coraltidemowing.com</p>
    <p class="contact__line">www.coraltidemowing.com</p>
  </div>

  <div class="services">
    <h2 class="services__title">SERVICES</h2>
    <ul class="services__list">
      <li>Garden maintenance</li>
      <li>Rubbish removal</li>
      <li>Trimming</li>
      <li>Weeding</li>
      <li>Lawn care</li>
    </ul>
  </div>
</section>

</body>
</html>
```